Consulting/Brand Licensing business needs business card

We need a business card created for our IP company, that also does consulting and brand licensing. We would like this card to be vague, as our other business' are in the cannabis industry and this is a non-cannabis touching entity. Perhaps something that hints vaguely at the industry without alerting or possibly offending the receiver.

Target Market(s)

CEOs/Key Decision Makers/Industry Leaders

Contact Information for Business Card

No address, simply list Seattle, WA. Phone: 206-555-0143. Name: Dario Lindqvist // email: Dario@velmarcoast.com

Colors

Designer to choose colors to be used in the design.

Requirements
Must have
• Logo, Name, Email, Phone number, "Consulting, Licensing and Branding Specialists"
Nice to have
• We would like this to be more professional than playful.

```html
<!DOCTYPE html>
<html lang="en">
<head>
<meta charset="utf-8">
<title>Velmar Coast, Inc — Business Card</title>
<link rel="stylesheet" href="https://fonts.googleapis.com/css2?family=Open+Sans:wght@400;700&display=swap">
<style>
  :root {
    --stage: #212121;
    --brand-orange: #df4d2e;
    --paper: #ffffff;
    --ink: #333333;
    --rule: #8a8a8a;
  }
  * { margin: 0; padding: 0; box-sizing: border-box; }
  html, body { width: 1200px; height: 1200px; overflow: hidden; }
  body {
    background: var(--stage);
    position: relative;
    font-family: "Open Sans", Arial, sans-serif;
  }
  .card {
    position: absolute;
    left: 187px;
    width: 840px;
    height: 480px;
  }

  /* Front */
  .card-front {
    top: 106px;
    background: var(--brand-orange);
    color: var(--paper);
  }
  .front-lockup {
    position: absolute;
    left: 0;
    right: 0;
    top: 180px;
    text-align: center;
  }
  .wordmark-front {
    font-weight: 700;
    font-size: 56px;
    line-height: 1.1;
    letter-spacing: 0.5px;
    white-space: nowrap;
  }
  .tagline-front {
    margin-top: 38px;
    font-weight: 400;
    font-size: 20px;
    letter-spacing: 0.6px;
    white-space: nowrap;
  }

  /* Back */
  .card-back {
    top: 644px;
    background: var(--paper);
    border-bottom: 7px solid var(--brand-orange);
  }
  .wordmark-back {
    position: absolute;
    left: 139px;
    top: 172px;
    width: 236px;
    height: 144px;
    display: flex;
    align-items: center;
    justify-content: center;
    text-align: center;
    color: var(--brand-orange);
    font-weight: 700;
    font-size: 36px;
    line-height: 1.2;
    white-space: nowrap;
  }
  .divider {
    position: absolute;
    left: 444px;
    top: 159px;
    width: 1.5px;
    height: 158px;
    background: var(--rule);
  }
  .contact {
    position: absolute;
    left: 476px;
    top: 152px;
    color: var(--ink);
  }
  .contact-name {
    font-weight: 700;
    font-size: 27px;
    letter-spacing: 0.5px;
    line-height: 1.2;
  }
  .contact-city {
    font-size: 19px;
    margin-top: 8px;
    letter-spacing: 0.3px;
    line-height: 1.3;
  }
  .contact-line {
    display: flex;
    align-items: center;
    gap: 15px;
    font-size: 16px;
    letter-spacing: 0.8px;
  }
  .contact-line.phone { margin-top: 18px; }
  .contact-line.email { margin-top: 15px; }
  .icon-badge {
    width: 32px;
    height: 32px;
    border-radius: 50%;
    background: var(--brand-orange);
    display: flex;
    align-items: center;
    justify-content: center;
    flex: none;
  }
</style>
</head>
<body>
  <section class="card card-front">
    <div class="front-lockup">
      <div class="wordmark-front">Velmar Coast, Inc</div>
      <div class="tagline-front">Consulting, Licensing and Branding Specialists</div>
    </div>
  </section>

  <section class="card card-back">
    <div class="wordmark-back">Velmar Coast,<br>Inc</div>
    <div class="divider"></div>
    <div class="contact">
      <div class="contact-name">Dario Lindqvist</div>
      <div class="contact-city">Seattle, WA</div>
      <div class="contact-line phone">
        <span class="icon-badge">
          <svg width="16" height="16" viewBox="0 0 24 24" aria-hidden="true">
            <path fill="#fff" d="M6.6 10.8a15.1 15.1 0 0 0 6.6 6.6l2.2-2.2a1 1 0 0 1 1-.25 11.4 11.4 0 0 0 3.6.57 1 1 0 0 1 1 1V20a1 1 0 0 1-1 1A17 17 0 0 1 3 4a1 1 0 0 1 1-1h3.5a1 1 0 0 1 1 1c0 1.25.2 2.45.57 3.57a1 1 0 0 1-.25 1z"/>
          </svg>
        </span>
        <span>206-555-0143</span>
      </div>
      <div class="contact-line email">
        <span class="icon-badge">
          <svg width="16" height="12" viewBox="0 0 16 12" aria-hidden="true">
            <rect x="0.75" y="0.75" width="14.5" height="10.5" fill="none" stroke="#fff" stroke-width="1.5"/>
            <path d="M1 1l7 5.5L15 1" fill="none" stroke="#fff" stroke-width="1.5"/>
          </svg>
        </span>
        <span>Dario@velmarcoast.com</span>
      </div>
    </div>
  </section>
</body>
</html>
```